Kelvar Systems Sdn. Bhd. - logo/ B.Card and letter head
Kelvar Systems Sdn. Bhd.
Kelvar Systems Sdn. Bhd. - logo/ B.Card and letter head - Information Technology
Creative Brief
Professional
Daniel Loh
Director
Lot B14, Second Floor, East Block Meridian Shopping Mall, Jalan Cempaka 7/3, Taman Sri Kenari, 43200 Cheras, Selangor D.E
daniel.loh@kelvarplay.com
512863 - P
The name and designation will be updated later. Please include the font type on on the design upon confirmation of the design. KVS is Information technology which is specilaise in lottery and gaming business so the designer will think a logo for us. You need to specific to the designer that you need a logo
will be updated later when everything had been finalized.

```html
<!DOCTYPE html>
<html lang="en">
<head>
<meta charset="utf-8">
<title>Kelvar Systems Sdn. Bhd. – Business Card</title>
<link href="https://fonts.googleapis.com/css2?family=Arimo:wght@400;700&display=swap" rel="stylesheet">
<style>
  :root {
    --brand-red: #a8141f;
    --card-grey: #e5e1da;
    --ink-white: #ffffff;
    --page-bg: #d9d6d1;
  }
  * { box-sizing: border-box; margin: 0; padding: 0; }
  html, body { width: 1200px; height: 850px; overflow: hidden; }
  body {
    background: var(--page-bg);
    font-family: "Arimo", Arial, sans-serif;
    position: relative;
  }
  .card {
    position: absolute;
    width: 590px;
    height: 340px;
    border-radius: 16px;
    overflow: hidden;
    background: var(--card-grey);
    box-shadow: 0 4px 14px rgba(0,0,0,0.18);
  }
  .card--front { left: 200px; top: 48px; }
  .card--back  { left: 410px; top: 462px; }
  .card__shape { position: absolute; inset: 0; width: 100%; height: 100%; }

  .contact {
    position: absolute;
    left: 40px;
    top: 32px;
    color: var(--ink-white);
  }
  .contact__name { font-size: 19px; font-weight: 400; line-height: 1.15; }
  .contact__title { font-size: 13px; margin-bottom: 16px; }
  .contact__address { font-size: 12px; line-height: 1.45; margin-bottom: 10px; }
  .contact__line {
    display: flex; align-items: center; gap: 10px;
    font-size: 12px; line-height: 1.6;
  }
  .contact__icon { width: 12px; height: 12px; fill: var(--ink-white); flex: none; }

  .wordmark { position: absolute; color: var(--ink-white); font-weight: 700; }
  .wordmark__initials { display: block; letter-spacing: -2px; line-height: 0.9; }
  .wordmark__name { display: block; white-space: nowrap; }

  .card--front .wordmark { left: 338px; top: 44px; }
  .card--front .wordmark__initials { font-size: 68px; }
  .card--front .wordmark__name { font-size: 14px; margin-top: 6px; }

  .card--back .wordmark { left: 62px; top: 100px; }
  .card--back .wordmark__initials { font-size: 96px; }
  .card--back .wordmark__name { font-size: 18px; margin-top: 8px; }
</style>
</head>
<body>

<section class="card card--front" aria-label="Business card front">
  <svg class="card__shape" viewBox="0 0 590 340" preserveAspectRatio="none" aria-hidden="true">
    <polygon points="0,0 565,0 530,200 0,360" fill="var(--brand-red)"/>
    <circle cx="520" cy="268" r="52" fill="var(--brand-red)"/>
  </svg>

  <div class="contact">
    <p class="contact__name">Daniel Loh</p>
    <p class="contact__title">Director</p>
    <p class="contact__address">
      Lot B14, Second Floor,<br>
      East Block Meridian Shopping Mall,<br>
      Jalan Cempaka 7/3,<br>
      Taman Sri Kenari,<br>
      43200 Cheras, Selangor D.E
    </p>
    <p class="contact__line">
      <svg class="contact__icon" viewBox="0 0 24 24"><path d="M6.6 10.8a15 15 0 0 0 6.6 6.6l2.2-2.2c.3-.3.7-.4 1-.2 1.1.4 2.3.6 3.6.6.6 0 1 .4 1 1V20c0 .6-.4 1-1 1A17 17 0 0 1 3 4c0-.6.4-1 1-1h3.5c.6 0 1 .4 1 1 0 1.3.2 2.5.6 3.6.1.3 0 .7-.2 1z"/></svg>
      03 - 5182 6407
    </p>
    <p class="contact__line">
      <svg class="contact__icon" viewBox="0 0 24 24"><path d="M6 3h10v5H6zM4 9h16a2 2 0 0 1 2 2v6h-4v4H6v-4H2v-6a2 2 0 0 1 2-2zm4 7v3h8v-3z"/></svg>
      03 - 5182 6419
    </p>
    <p class="contact__line">
      <svg class="contact__icon" viewBox="0 0 24 24"><path d="M2 5h20v14H2zm2 2v.5l8 5 8-5V7l-8 5z"/></svg>
      daniel.loh@kelvarplay.com
    </p>
  </div>

  <div class="wordmark">
    <span class="wordmark__initials">KVS</span>
    <span class="wordmark__name">Kelvar Systems Sdn. Bhd.</span>
  </div>
</section>

<section class="card card--back" aria-label="Business card back">
  <svg class="card__shape" viewBox="0 0 590 340" preserveAspectRatio="none" aria-hidden="true">
    <polygon points="0,0 560,0 520,170 0,330" fill="var(--brand-red)"/>
    <circle cx="508" cy="268" r="54" fill="var(--brand-red)"/>
  </svg>

  <div class="wordmark">
    <span class="wordmark__initials">KVS</span>
    <span class="wordmark__name">Kelvar Systems Sdn. Bhd.</span>
  </div>
</section>

</body>
</html>
```